Exciting new aperitif brand needs a great label

Vel-Orin is a wonderful rich new premium-priced bitter aperitif, with a deep red colour, from a 100+ year old distillery (1890) near Turin in the Piedmont region of Italy. Inspired by Torvesi, it is perfectly formulated to elevate the classic Baldetti cocktail (and variations on it). It also goes perfectly in a Spritz or a long mixed drink with soda or tonic. The name Vel-Orin is derived from the French for 'peak' and the Italian word for 'love'.

The label, which should take inspiration from Torvesi, but be distinctively different, can incoporate any number of premium label embellishments (foil, embossing, textures etc) and should be no greater than 11cm (height) x 9cm (width) with any core imagery restricted to a width of c.7cm.

The attached mood board should act as inspiration and colour should largely be restricted to reds, blues, whites and perhaps orange. For completeness, the label should note that the ABV is 25% and the bottle size 70cl.

Target Market(s)

21-45yr olds - equal split female/male

Colors
0054AA
0677BA
7BADD7
CADEEF
E8F1F8
0094D4
00A9DD
6FCCEA
C7EBF8
E9F6FB
EE7325
F08F49
F5BC92
FAE3D3
FDF4ED
EB3D1F
EC4F4E
F09395
F8D3D4
FCEDEE

Requirements
Must have
• Great lettering design on the name Vel-Orin

```html
<!DOCTYPE html>
<html lang="en">
<head>
<meta charset="utf-8">
<title>Vel-Orin Bitter Aperitivo Label</title>
<link rel="stylesheet" href="https://fonts.googleapis.com/css2?family=Alfa+Slab+One&family=Roboto+Slab:wght@300;700&family=Great+Vibes&display=swap">
<style>
  :root{
    --gold:#d9a441;
    --gold-deep:#b8732a;
    --gold-light:#f6d77a;
    --orange:#e08a12;
    --navy:#010a22;
    --navy-mid:#0a1236;
    --sky:#00a9dd;
    --blue:#0677ba;
    --blue-deep:#0054aa;
    --paper:#ffffff;
    --paper-shade:#ececec;
    --snow:#e8f1f8;
  }
  html,body{margin:0;padding:0;overflow:hidden;background:var(--paper);}
  .label{display:block;width:982px;height:1200px;}
  .abv{font-family:"Alfa Slab One",serif;font-size:46px;letter-spacing:14px;fill:url(#abvGold);}
  .brand-name{font-family:"Roboto Slab",serif;font-weight:700;font-size:420px;fill:var(--paper);}
  .tagline{font-family:"Roboto Slab",serif;font-weight:300;font-size:30px;fill:url(#goldRun);}
  .origin{font-family:"Great Vibes",cursive;font-size:58px;fill:url(#abvGold);}
</style>
</head>
<body>
<svg class="label" viewBox="0 0 982 1200" xmlns="http://www.w3.org/2000/svg">
  <defs>
    <linearGradient id="frameGold" x1="0" y1="0" x2="1" y2="1">
      <stop offset="0" stop-color="#f3c35a"/>
      <stop offset=".5" stop-color="#c98a3a"/>
      <stop offset="1" stop-color="#e8b04a"/>
    </linearGradient>
    <linearGradient id="goldRun" x1="0" y1="0" x2="1" y2="0">
      <stop offset="0" stop-color="#c68a2c"/>
      <stop offset=".5" stop-color="#f6d77a"/>
      <stop offset="1" stop-color="#e07a22"/>
    </linearGradient>
    <linearGradient id="abvGold" x1="0" y1="0" x2="1" y2="0">
      <stop offset="0" stop-color="#e08a12"/>
      <stop offset=".5" stop-color="#f0b81a"/>
      <stop offset="1" stop-color="#b8862a"/>
    </linearGradient>
    <radialGradient id="nightGlow" cx=".5" cy=".4" r=".7">
      <stop offset="0" stop-color="#020f33"/>
      <stop offset=".7" stop-color="#010a22"/>
      <stop offset="1" stop-color="#2a1410"/>
    </radialGradient>
    <linearGradient id="skyBand" x1="0" y1="0" x2="1" y2="0">
      <stop offset="0" stop-color="#0094d4"/>
      <stop offset=".4" stop-color="#00a9dd"/>
      <stop offset="1" stop-color="#0677ba"/>
    </linearGradient>
    <linearGradient id="peaks" x1="0" y1="0" x2="0" y2="1">
      <stop offset="0" stop-color="#e8f1f8"/>
      <stop offset=".45" stop-color="#7badd7"/>
      <stop offset="1" stop-color="#0b3f6e"/>
    </linearGradient>
    <linearGradient id="cornerGold" x1="0" y1="0" x2="1" y2="1">
      <stop offset="0" stop-color="#f2c65c" stop-opacity=".55"/>
      <stop offset="1" stop-color="#c98a3a" stop-opacity=".15"/>
    </linearGradient>
  </defs>

  <rect class="frame" x="0" y="0" width="982" height="1200" fill="url(#frameGold)"/>
  <rect class="paper" x="14" y="14" width="954" height="1186" fill="var(--paper)"/>

  <g class="chevron-rules" fill="none">
    <polyline points="14,150 494,10 968,150" stroke="var(--paper-shade)" stroke-width="2"/>
    <polyline points="14,181 494,41 968,181" stroke="var(--gold)" stroke-width="1.5"/>
    <polyline points="14,220 494,80 968,220" stroke="var(--paper-shade)" stroke-width="2"/>
    <polyline points="14,259 494,119 968,259" stroke="var(--gold-deep)" stroke-width="2"/>
    <polyline points="14,305 494,165 968,305" stroke="var(--gold-deep)" stroke-width="3"/>
  </g>

  <rect class="corner-flourish" x="38" y="38" width="180" height="180" fill="url(#cornerGold)" role="img" aria-label="Gold filigree corner ornament"/>
  <rect class="corner-flourish" x="764" y="38" width="180" height="180" fill="url(#cornerGold)" role="img" aria-label="Gold filigree corner ornament"/>

  <text class="abv" x="491" y="86" text-anchor="middle">25% ABV</text>

  <rect class="sky-band" x="14" y="840" width="954" height="360" fill="url(#skyBand)"/>
  <g class="sky-rules" fill="none" stroke="#6fccea" stroke-opacity=".45" stroke-width="2">
    <line x1="14" y1="900" x2="480" y2="1040"/>
    <line x1="14" y1="950" x2="400" y2="1065"/>
    <line x1="968" y1="900" x2="520" y2="1040"/>
    <line x1="968" y1="950" x2="600" y2="1065"/>
  </g>

  <polygon class="night-field" points="0,357 494,208 982,357 982,849 494,1000 0,849" fill="url(#nightGlow)"/>
  <g class="hex-rules" fill="none" stroke="url(#goldRun)" stroke-width="3">
    <polyline points="40,390 494,257 942,390"/>
    <polyline points="40,809 494,928 942,809"/>
  </g>

  <text class="brand-name" x="491" y="722" text-anchor="middle" textLength="900" lengthAdjust="spacingAndGlyphs">Vel-Orin</text>

  <text class="tagline" x="486" y="781" text-anchor="middle" textLength="854" lengthAdjust="spacing">BITTER  APERITIVO</text>

  <rect class="peaks-art" x="14" y="960" width="954" height="240" fill="url(#peaks)" role="img" aria-label="Snow-capped blue mountain range with a golden heart on the highest peak"/>

  <text class="origin" x="491" y="1172" text-anchor="middle">Made In Italy</text>
</svg>
</body>
</html>
```